professional business card

A Clean looking business card for a money transfer company. Our company is call Velorix= Transfer + Send = Transcend (next level)
to show professionalism as well as some effects to show digital tech.

1 side to have position, name and address
2 side to have company name and show that we provide money exchange and cross-border money transfer

Target Market(s)

Remittance companies and high net worth individuals

Industry/Entity Type

Finance

Contact Information for Business Card

Name, address, email, title, services- money exchange and cross-border remittance

Requirements
Nice to have
• Digital age feel

```html
<!DOCTYPE html>
<html lang="en">
<head>
<meta charset="utf-8">
<title>Velorix Business Card</title>
<link href="https://fonts.googleapis.com/css2?family=Open+Sans:wght@400;600;700&display=swap" rel="stylesheet">
<style>
  :root {
    --stage: #222222;
    --card: #243140;
    --card-deep: #1b2531;
    --accent: #5fc3d3;
    --ink: #ffffff;
    --ink-soft: #d9e0e6;
    --emboss: #1a2430;
  }
  * { margin: 0; padding: 0; box-sizing: border-box; }
  html, body { width: 1200px; height: 780px; overflow: hidden; }
  body {
    background: var(--stage);
    font-family: "Open Sans", Arial, sans-serif;
    position: relative;
  }
  .card {
    position: absolute;
    top: 236px;
    width: 540px;
    height: 308px;
    background: var(--card);
    overflow: hidden;
    box-shadow: 0 18px 40px rgba(0,0,0,0.45);
  }
  .card--contact { left: 40px; }
  .card--brand { left: 620px; }

  /* contact side */
  .contact-block {
    position: absolute;
    left: 34px;
    top: 34px;
    padding-left: 16px;
    color: var(--ink-soft);
  }
  .contact-block::before {
    content: "";
    position: absolute;
    left: 0; top: 2px;
    width: 6px; height: 28px;
    background: var(--accent);
  }
  .person-name {
    font-size: 27px;
    font-weight: 700;
    color: var(--accent);
    line-height: 1.15;
  }
  .person-title {
    font-size: 14px;
    font-weight: 600;
    color: var(--ink);
    margin-bottom: 10px;
  }
  .address { font-size: 13px; line-height: 1.45; margin-bottom: 8px; }
  .contact-list { list-style: none; font-size: 13px; line-height: 1.55; }
  .contact-list li { display: flex; align-items: center; gap: 7px; }
  .contact-list svg { width: 12px; height: 12px; fill: var(--accent); flex: none; }
  .emboss-name {
    position: absolute;
    right: 26px;
    bottom: 18px;
    font-size: 46px;
    font-weight: 700;
    letter-spacing: 2px;
    color: var(--emboss);
  }

  /* brand side */
  .texture {
    position: absolute;
    inset: 0;
    background: linear-gradient(100deg, #222d3a 0%, #263443 55%, #4a5866 85%, #8c97a2 100%);
  }
  .brand-lockup {
    position: absolute;
    left: 0; right: 0;
    top: 96px;
    display: flex;
    justify-content: center;
    align-items: center;
    gap: 14px;
  }
  .brand-mark { width: 26px; height: 26px; background: var(--accent); }
  .brand-name {
    font-size: 52px;
    font-weight: 700;
    letter-spacing: 3px;
    color: var(--ink);
  }
  .services {
    position: absolute;
    left: 0; right: 0;
    top: 184px;
    display: flex;
    justify-content: center;
    align-items: center;
    gap: 10px;
    font-size: 14px;
    color: var(--ink);
  }
  .services-label { color: var(--accent); letter-spacing: 1px; }
  .services-dot { width: 7px; height: 7px; background: var(--accent); }
</style>
</head>
<body>

  <section class="card card--contact" aria-label="Contact side">
    <div class="contact-block">
      <h1 class="person-name">Mara Kolvenko</h1>
      <p class="person-title">Managing Director</p>
      <p class="address">418 Harlow Ave. Suite 310<br>Ashford, TX 75090</p>
      <ul class="contact-list">
        <li>
          <svg viewBox="0 0 24 24" aria-hidden="true"><path d="M6.6 10.8a15.1 15.1 0 0 0 6.6 6.6l2.2-2.2c.3-.3.7-.4 1-.2 1.1.4 2.3.6 3.6.6.6 0 1 .4 1 1V20c0 .6-.4 1-1 1C10.6 21 3 13.4 3 4c0-.6.4-1 1-1h3.5c.6 0 1 .4 1 1 0 1.3.2 2.5.6 3.6.1.3 0 .7-.2 1z"/></svg>
          (555) 014-3827
        </li>
        <li>
          <svg viewBox="0 0 24 24" aria-hidden="true"><path d="M3 5h18v14H3z M3 5l9 7 9-7" fill="none" stroke="#5fc3d3" stroke-width="2"/></svg>
          info@velorix-mail.com
        </li>
        <li>
          <svg viewBox="0 0 24 24" aria-hidden="true"><circle cx="12" cy="12" r="9" fill="none" stroke="#5fc3d3" stroke-width="2"/><path d="M3 12h18M12 3c3 3 3 15 0 18M12 3c-3 3-3 15 0 18" fill="none" stroke="#5fc3d3" stroke-width="1.6"/></svg>
          www.velorix-pay.com
        </li>
      </ul>
    </div>
    <p class="emboss-name">VELORIX</p>
  </section>

  <section class="card card--brand" aria-label="Brand side">
    <div class="texture" role="img" aria-label="Repeating brand pattern fading from dark navy to silver toward the right edge"></div>
    <div class="brand-lockup">
      <span class="brand-mark" aria-hidden="true"></span>
      <span class="brand-name">VELORIX</span>
    </div>
    <div class="services">
      <span class="services-label">SERVICES</span>
      <span class="services-dot" aria-hidden="true"></span>
      <span>Money exchange</span>
      <span class="services-dot" aria-hidden="true"></span>
      <span>Cross-border remittance</span>
    </div>
  </section>

</body>
</html>
```